Postcard to alert practices of a new dermatology practice opening

We are opening a dermatology practice and need a front and back postcard that we can drop off to practices and friends to alert them of our opening, as well as what we offer:
Would like the colors to be bright nice blue, white, and dark gray.
Also - i am attaching the logo we already have (would like the card to be more of a blue color - not the logo color ), an example of a flyer, and a picture of me to add to the postcard mailer

Front of card:
Verandell Dermatology and Skin Surgery Associates

Now scheduling appointments. Call us (555)-014-7280!

Specializing in
- Mohs surgery by a Fellowship-Trained Mohs Surgeon
- Comprehensive dermatologic care including medical, cosmetic and surgical dermatology
- Individualized care for every patient using state of the art techniques

Corinne T. Valdemar, MD, FAAD
Board-Certified Dermatologist and Fellowship-Trained Mohs Surgeon

Dr. Valdemar graduated from the Brackenfield State University Medical School, Sigma Rho Delta, and completed her dermatology residency and Mohs fellowship at Whitcombe University in Atlanta GA. She provides complete dermatologic care for the whole family with a specialization in Mohs surgery.

4471 Quillan Avenue, Suite 100
Charlotte, NC 28999
Tel. (555)-014-7280
Fax. (555) 014-5193
www.VerandellDermatology.example

Please add logos for NGSM, CUCS, FBMS (can find on my webpage the logos)

Back of card:
About Dr. Valdemar
Dr. Corinne Tolliver Valdemar is a Board-Certified Dermatologist and Fellowship-Trained Mohs Surgeon from Whitcombe University. She graduated Tau Zeta Mu and with highest distinction from the Brackenfield State University. She then received her M.D. and Master’s in Public Health from the Brackenfield State University School of Medicine. Graduating at the top of her class, Dr. Valdemar was inducted into the prestigious Sigma Rho Delta honor society, which is the highest academic honor in medical school.

Dr. Valdemar completed her internship at Fernhollow hospital in Salt Lake City, Utah. She completed her dermatology residency training at Whitcombe University School of Medicine, serving as the Chief Resident during her final year. During her time as a resident, she received the CUCS resident scholarship award and worked with leading experts in both cutaneous and transplant oncology.
After her residency she went on to receive highly competitive sub-specialty training and completed her fellowship training in Mohs Micrographic Surgery, Cutaneous Oncology, and Reconstructive Surgery at Whitcombe University Department of Dermatology. This Procedural Dermatology fellowship is certified both by the Federated Board of Margin Surgery (FBMS) and the Physicians’ League Oversight Board for Residency Training (PLOBRT). During her training Dr. Valdemar performed thousands of dermatologic surgeries.

She has authored numerous scientific articles and textbook chapters, spoken at national meetings and served on numerous committees. Dr. Valdemar is Board Certified in Dermatology and is a Fellow of the National Guild of Skin Medicine and Federated Board of Margin Surgery. She is a member of the National Guild of Skin Medicine, Continental Union of Cutaneous Surgery, Lantern Circle Skin Society, Global Graft Recipient Melanoma Network, Sigma Rho Delta National Honor Society, and Piedmont Skin Physicians Alliance.

Prior to moving back to North Carolina, she practiced with Riverbend Skin Partners in Cincinnati performing Mohs surgery, skin surgeries, general dermatology, and cosmetics.

also put map of location and contact information for practice again.

Font styles to use
Serif

Colors
0455a3
ffffff
919191

Requirements
Must have
• on the back of the card - put a map of the practice as well as my about dr. valdemar
• front of the card - multiple pictures (can take from my website) and information about what I specialize in, location, phone number, website
Nice to have
• would like it simple and clean just like the example I provided. Mostly white background with font in a nice blue color and a dark grey. with simple clean lines
Should not have
• DO NOT put my face on the front of the card - should only be on back of card
• DO NOT put lines on the back of the card - i will not be mailing these
• DO NOT add fancy bullets

```html
<!DOCTYPE html>
<html lang="en">
<head>
<meta charset="utf-8">
<title>Verandell Dermatology – Opening Postcard</title>
<link rel="stylesheet" href="https://fonts.googleapis.com/css2?family=Source+Sans+3:wght@400;600;700&display=swap">
<style>
  :root {
    --blue-deep: #1b6db3;
    --blue-bright: #2aa5df;
    --blue-head: #2a9ad6;
    --blue-text: #1b6db3;
    --grey-text: #4a4a4a;
    --grey-line: #919191;
    --white: #ffffff;
    --page: #e9e9e9;
  }
  * { box-sizing: border-box; margin: 0; padding: 0; }
  html, body { width: 1006px; height: 1200px; overflow: hidden; background: var(--page); }
  body { font-family: "Source Sans 3", Arial, sans-serif; color: var(--grey-text); }
  .stage { position: absolute; left: 0; top: 0; width: 1113px; height: 1328px; transform: scale(0.9039); transform-origin: 0 0; }
  .card { position: absolute; background: var(--white); box-shadow: 0 3px 10px rgba(0,0,0,.25); overflow: hidden; }
  .card--front { left: 134px; top: 85px; width: 861px; height: 560px; }
  .card--back { left: 133px; top: 692px; width: 864px; height: 558px; }
  .abs { position: absolute; }

  .photo { position: absolute; }
  .photo--family { left: 0; top: 0; width: 218px; height: 183px; background: linear-gradient(135deg, #7c9a3c, #5a3a28 60%, #c88f66); }
  .photo--facial { left: 222px; top: 0; width: 164px; height: 183px; background: linear-gradient(160deg, #f2e1d6, #d9b8a3); }
  .photo--lab { left: 0; top: 187px; width: 165px; height: 185px; background: linear-gradient(135deg, #b9d4e6, #4fa7c9 70%, #2c6e8a); }
  .photo--couple { left: 168px; top: 187px; width: 218px; height: 185px; background: linear-gradient(135deg, #f1f1f1, #d7b39a 55%, #8a6a55); }
  .photo--skin { left: 0; top: 376px; width: 219px; height: 184px; background: linear-gradient(160deg, #f6f6f6, #e6cbb9); }
  .photo--exam { left: 222px; top: 376px; width: 164px; height: 184px; background: linear-gradient(135deg, #c89a7f, #8b5f4a 60%, #e9e2dc); }

  .brand { position: absolute; display: flex; align-items: center; gap: 10px; color: var(--blue-bright); font-weight: 400; }
  .brand__dot { width: 58px; height: 58px; border: 3px solid var(--blue-bright); border-radius: 50%; flex: none; }
  .brand__name { font-size: 27px; line-height: 25px; }
  .brand--front { left: 435px; top: 30px; }
  .brand--back { left: 518px; top: 455px; }
  .brand--back .brand__dot { width: 48px; height: 48px; }
  .brand--back .brand__name { font-size: 22px; line-height: 21px; }

  .band-open { left: 386px; top: 104px; width: 474px; height: 71px; background: var(--blue-deep); color: var(--white); display: flex; flex-direction: column; align-items: center; justify-content: center; }
  .band-open__title { font-weight: 700; font-size: 36px; line-height: 38px; letter-spacing: 1px; }
  .band-open__call { font-size: 15px; line-height: 18px; letter-spacing: .2px; }

  .specialties { left: 406px; top: 188px; width: 440px; }
  .specialties__title { color: var(--blue-head); font-weight: 700; font-size: 23px; line-height: 28px; letter-spacing: .3px; margin-bottom: 4px; }
  .specialties__list { list-style: none; font-size: 16px; line-height: 20.5px; color: var(--grey-text); }
  .specialties__list li { position: relative; padding-left: 20px; }
  .specialties__list svg { position: absolute; left: 2px; top: 5px; }

  .portrait { border-radius: 50%; background: radial-gradient(circle at 50% 40%, #c9a592, #5d4035 75%); box-shadow: 0 0 0 3px var(--white), 0 0 0 5px var(--blue-deep); }
  .portrait--front { left: 406px; top: 345px; width: 74px; height: 74px; }
  .doctor { left: 506px; top: 356px; color: var(--blue-text); font-size: 15px; line-height: 16.5px; }
  .doctor__name { font-weight: 700; text-transform: uppercase; }
  .bio { left: 417px; top: 433px; width: 422px; font-size: 12.3px; line-height: 12.8px; text-align: justify; color: var(--grey-text); }

  .band-address { left: 386px; top: 502px; width: 474px; height: 58px; background: var(--blue-deep); color: var(--white); font-size: 18.5px; letter-spacing: .3px; display: flex; align-items: center; padding-left: 24px; gap: 12px; }

  .band-about { left: 0; top: 28px; width: 400px; height: 77px; background: var(--blue-bright); color: var(--white); font-weight: 700; font-size: 23.5px; display: flex; align-items: center; padding-left: 45px; }
  .portrait--back { left: 355px; top: 22px; width: 106px; height: 106px; box-shadow: 0 0 0 5px var(--white), 0 0 0 8px var(--blue-deep); }
  .about { left: 25px; top: 140px; width: 436px; font-size: 11.45px; line-height: 12.55px; text-align: justify; color: var(--grey-text); }
  .about p.gap { margin-top: 12px; }

  .contact { left: 495px; top: 28px; font-size: 11.5px; line-height: 16.6px; color: var(--grey-text); }
  .contact__row { display: flex; gap: 8px; }
  .contact__row svg { margin-top: 2px; flex: none; }
  .contact__indent { padding-left: 16px; }
  .stamp { left: 747px; top: 28px; width: 93px; height: 69px; border: 1px solid var(--grey-line); }
  .map { left: 495px; top: 125px; width: 345px; height: 300px; background: linear-gradient(135deg, #e8eef2, #d5e2d0 55%, #cfdbe6); border: 1px solid #d0d6db; }
  .band-foot { left: 0; top: 530px; width: 864px; height: 28px; background: var(--blue-deep); }
</style>
</head>
<body>
<div class="stage">

  <section class="card card--front">
    <div class="photo photo--family" role="img" aria-label="Photo of a smiling family outdoors"></div>
    <div class="photo photo--facial" role="img" aria-label="Photo of a woman with facial contour guide lines"></div>
    <div class="photo photo--lab" role="img" aria-label="Photo of a masked clinician at a microscope"></div>
    <div class="photo photo--couple" role="img" aria-label="Photo of a smiling older couple"></div>
    <div class="photo photo--skin" role="img" aria-label="Photo of a woman with clear skin"></div>
    <div class="photo photo--exam" role="img" aria-label="Photo of a dermatoscope skin examination"></div>

    <div class="brand brand--front">
      <span class="brand__dot"></span>
      <span class="brand__name">Verandell Dermatology<br>and Skin Surgery Associates</span>
    </div>

    <div class="abs band-open">
      <div class="band-open__title">NOW OPEN</div>
      <div class="band-open__call">Now scheduling appointments. Call us (555)-014-7280!</div>
    </div>

    <div class="abs specialties">
      <h2 class="specialties__title">SPECIALIZING IN</h2>
      <ul class="specialties__list">
        <li><svg width="11" height="11" viewBox="0 0 11 11"><circle cx="5.5" cy="5.5" r="4.6" fill="none" stroke="#2a9ad6" stroke-width="1.1"/><path d="M3.2 5.6l1.6 1.6 3-3" fill="none" stroke="#2a9ad6" stroke-width="1.2"/></svg>Mohs surgery by a Fellowship-Trained Mohs Surgeon</li>
        <li><svg width="11" height="11" viewBox="0 0 11 11"><circle cx="5.5" cy="5.5" r="4.6" fill="none" stroke="#2a9ad6" stroke-width="1.1"/><path d="M3.2 5.6l1.6 1.6 3-3" fill="none" stroke="#2a9ad6" stroke-width="1.2"/></svg>Comprehensive dermatologic care including medical, cosmetic and surgical dermatology</li>
        <li><svg width="11" height="11" viewBox="0 0 11 11"><circle cx="5.5" cy="5.5" r="4.6" fill="none" stroke="#2a9ad6" stroke-width="1.1"/><path d="M3.2 5.6l1.6 1.6 3-3" fill="none" stroke="#2a9ad6" stroke-width="1.2"/></svg>Individualized care for every patient using state of the art techniques</li>
      </ul>
    </div>

    <div class="abs portrait portrait--front" role="img" aria-label="Portrait of Dr. Valdemar"></div>
    <div class="abs doctor">
      <div class="doctor__name">Corinne T. Valdemar, MD, FAAD</div>
      <div>Board-Certified Dermatologist and<br>Fellowship-Trained Mohs Surgeon</div>
    </div>

    <p class="abs bio">Dr. Valdemar graduated from the Brackenfield State University Medical School, Sigma Rho Delta, and completed her dermatology residency and Mohs fellowship at Whitcombe University in Atlanta GA. She provides complete dermatologic care for the whole family with a specialization in Mohs surgery.</p>

    <div class="abs band-address">
      <svg width="13" height="17" viewBox="0 0 13 17"><path d="M6.5 0C2.9 0 0 2.8 0 6.3 0 10.8 6.5 17 6.5 17S13 10.8 13 6.3C13 2.8 10.1 0 6.5 0z" fill="#fff"/><circle cx="6.5" cy="6.3" r="2.4" fill="#1b6db3"/></svg>
      <span>4471 Quillan Avenue, Suite 100 Charlotte, NC 28999</span>
    </div>
  </section>

  <section class="card card--back">
    <div class="abs band-about">About Dr. Valdemar</div>
    <div class="abs portrait portrait--back" role="img" aria-label="Portrait of Dr. Valdemar"></div>

    <div class="abs about">
      <p>Dr. Corinne Tolliver Valdemar is a Board-Certified Dermatologist and Fellowship-Trained Mohs Surgeon from Whitcombe University. She graduated Tau Zeta Mu and with highest distinction from the Brackenfield State University. She then received her M.D. and Master’s in Public Health from the Brackenfield State University School of Medicine. Graduating at the top of her class, Dr. Valdemar was inducted into the prestigious Sigma Rho Delta honor society, which is the highest academic honor in medical school.</p>
      <p>Dr. Valdemar completed her internship at Fernhollow hospital in Salt Lake City, Utah. She completed her dermatology residency training at Whitcombe University School of Medicine, serving as the Chief Resident during her final year. During her time as a resident, she received the CUCS resident scholarship award and worked with leading experts in both cutaneous and transplant oncology. After her residency she went on to receive highly competitive sub-specialty training and completed her fellowship training in Mohs Micrographic Surgery, Cutaneous Oncology, and Reconstructive Surgery at Whitcombe University Department of Dermatology. This Procedural Dermatology fellowship is certified both by the Federated Board of Margin Surgery (FBMS) and the Physicians’ League Oversight Board for Residency Training (PLOBRT). During her training Dr. Valdemar performed thousands of dermatologic surgeries.</p>
      <p class="gap">She has authored numerous scientific articles and textbook chapters, spoken at national meetings and served on numerous committees. Dr. Valdemar is Board Certified in Dermatology and is a Fellow of the National Guild of Skin Medicine and Federated Board of Margin Surgery. She is a member of the National Guild of Skin Medicine, Continental Union of Cutaneous Surgery, Lantern Circle Skin Society, Global Graft Recipient Melanoma Network, Sigma Rho Delta National Honor Society, and Piedmont Skin Physicians Alliance. Prior to moving back to North Carolina, she practiced with Riverbend Skin Partners in Cincinnati performing Mohs surgery, skin surgeries, general dermatology, and cosmetics.</p>
    </div>

    <div class="abs contact">
      <div class="contact__row">
        <svg width="8" height="11" viewBox="0 0 13 17"><path d="M6.5 0C2.9 0 0 2.8 0 6.3 0 10.8 6.5 17 6.5 17S13 10.8 13 6.3C13 2.8 10.1 0 6.5 0z" fill="#1b6db3"/><circle cx="6.5" cy="6.3" r="2.4" fill="#fff"/></svg>
        <span>4471 Quillan Avenue, Suite 100</span>
      </div>
      <div class="contact__indent">Charlotte, NC 28999</div>
      <div class="contact__indent">Tel. (555)-014-7280</div>
      <div class="contact__indent">Fax. (555) 014-5193</div>
      <div class="contact__indent">www.VerandellDermatology.example</div>
    </div>

    <div class="abs stamp"></div>
    <div class="abs map" role="img" aria-label="Map showing the practice location on Quillan Avenue, Charlotte"></div>

    <div class="brand brand--back">
      <span class="brand__dot"></span>
      <span class="brand__name">Verandell Dermatology<br>and Skin Surgery Associates</span>
    </div>

    <div class="abs band-foot"></div>
  </section>

</div>
</body>
</html>
```